Business Card for supplement company

Company Name: Brimcrest Nutrition
We require quite a simple yet stand out business card for our supplement company.
We are selling high end bodybuilding supplements direct to the public through online sales and Facebook marketing.
There will be slightly varying versions of the card and the winning design will be required to make these slight adjustments.
We will also require the file to be provided in and editable version as we will have a discount code on there that will be changed for different people.
Employee Cards:
Logo on the front of the card (see attached EPS file)
Please also add slogan in text "When Failure is Not and Option" as close as possible to what is seen in this link www.brimcrestnutrition.example.com.au
Suggestions: Card in black, possibly use a similar background to website theme (honeycomb, carbon look)
Information to be included on the back (please place and order accordingly)
:Tarq Welmsby (Director)
Email: tarq@brimcrestnutrition.example.com.au
Phone: 02 5918 2273
Website: www.brimcrestnutrition.example.com.au
Athlete Cards:
Front:
Same as above
Back:
Discount Code: xxx123 (to be editable)
Facebook: www.socialsite.example/BrimcrestNutrition
Design ideas: please look at our website and facebook signup page for design ideas.

```html
<!DOCTYPE html>
<html lang="en">
<head>
<meta charset="utf-8">
<title>Brimcrest Nutrition – Business Cards</title>
<link rel="stylesheet" href="https://fonts.googleapis.com/css2?family=Exo+2:wght@300;400;600&display=swap">
<style>
  :root {
    --page-bg: #e4e6e8;
    --card-black: #0d0e0f;
    --card-grey: #1d1f21;
    --brand-green: #5fe02a;
    --brand-green-dark: #2f8f12;
    --text-white: #f2f2f2;
    --text-font: "Exo 2", sans-serif;
  }
  * { box-sizing: border-box; margin: 0; padding: 0; }
  html, body { width: 1200px; height: 1000px; overflow: hidden; }
  body {
    background: var(--page-bg);
    font-family: var(--text-font);
    position: relative;
  }
  .card {
    position: absolute;
    left: 220px;
    width: 760px;
    height: 434px;
    background: var(--card-black);
    overflow: hidden;
    box-shadow: 0 10px 24px rgba(0,0,0,0.25);
  }
  .card--employee { top: 36px; }
  .card--athlete { top: 530px; }
  .card-texture {
    position: absolute; inset: 0;
    background: radial-gradient(ellipse at 50% 45%, var(--card-grey) 0%, var(--card-black) 75%);
  }
  .swoosh { position: absolute; inset: 0; }
  .brand-name {
    position: absolute;
    color: var(--brand-green);
    font-weight: 600;
    text-transform: uppercase;
    line-height: 1;
  }
  .brand-name__main { display: block; letter-spacing: 2px; }
  .brand-name__sub { display: block; letter-spacing: 10px; }

  /* employee card */
  .card--employee .brand-name { left: 60px; top: 90px; }
  .card--employee .brand-name__main { font-size: 58px; }
  .card--employee .brand-name__sub { font-size: 20px; margin-top: 8px; letter-spacing: 12px; }
  .person { position: absolute; left: 520px; top: 128px; }
  .person__name {
    color: var(--brand-green); font-weight: 300; font-size: 24px;
    text-transform: uppercase; letter-spacing: 0.5px;
  }
  .person__role { color: var(--text-white); font-weight: 300; font-size: 15px; margin-top: 4px; }
  .contact-list { position: absolute; left: 466px; top: 226px; list-style: none; }
  .contact-list li {
    display: flex; align-items: center; gap: 9px;
    color: var(--text-white); font-weight: 300; font-size: 13.5px;
    height: 28px;
  }
  .contact-list svg { width: 15px; height: 15px; flex: none; }

  /* athlete card */
  .discount {
    position: absolute; right: 150px; top: 78px;
    color: var(--text-white); font-weight: 300; font-size: 17px;
  }
  .discount__code { color: var(--brand-green); }
  .card--athlete .brand-name { left: 0; right: 0; top: 128px; text-align: center; }
  .card--athlete .brand-name__main { font-size: 74px; }
  .card--athlete .brand-name__sub { font-size: 22px; margin-top: 10px; letter-spacing: 16px; }
  .website {
    position: absolute; left: 0; right: 0; top: 262px; text-align: center;
    color: var(--brand-green); font-weight: 400; font-size: 17px; letter-spacing: 3px;
  }
  .social {
    position: absolute; left: 150px; top: 320px;
    display: flex; align-items: center; gap: 12px;
    color: var(--brand-green); font-weight: 400; font-size: 17px;
  }
  .social__mark { width: 18px; height: 18px; background: var(--brand-green); flex: none; }
</style>
</head>
<body>

<section class="card card--employee" aria-label="Employee card">
  <div class="card-texture" role="img" aria-label="Dark honeycomb carbon texture"></div>
  <svg class="swoosh" viewBox="0 0 760 434" aria-hidden="true">
    <defs>
      <linearGradient id="swooshGreen" x1="0" y1="1" x2="1" y2="0">
        <stop offset="0" stop-color="#5fe02a" stop-opacity="0"/>
        <stop offset="0.45" stop-color="#2f8f12"/>
        <stop offset="1" stop-color="#5fe02a"/>
      </linearGradient>
    </defs>
    <path d="M120,372 C330,360 460,240 520,0 L566,0 C500,250 340,378 120,372 Z" fill="url(#swooshGreen)"/>
    <path d="M130,384 C350,376 500,250 576,0" fill="none" stroke="#ffffff" stroke-width="3"/>
  </svg>
  <div class="brand-name">
    <span class="brand-name__main">Brimcrest</span>
    <span class="brand-name__sub">Nutrition</span>
  </div>
  <div class="person">
    <p class="person__name">Tarq Welmsby</p>
    <p class="person__role">Director</p>
  </div>
  <ul class="contact-list">
    <li>
      <svg viewBox="0 0 16 16"><rect x="1" y="3" width="14" height="10" fill="var(--brand-green)"/><path d="M1,3 L8,9 L15,3" fill="none" stroke="#0d0e0f" stroke-width="1.4"/></svg>
      tarq@brimcrestnutrition.example.com.au
    </li>
    <li>
      <svg viewBox="0 0 16 16"><path d="M4,1 L6.5,4 L5,6 C6,8.5 7.5,10 10,11 L12,9.5 L15,12 L13,15 C7,14.5 1.5,9 1,3 Z" fill="var(--brand-green)"/></svg>
      02 5918 2273
    </li>
    <li>
      <svg viewBox="0 0 16 16"><circle cx="8" cy="8" r="6.5" fill="none" stroke="var(--brand-green)" stroke-width="1.5"/><path d="M1.5,8 H14.5 M8,1.5 C5,5 5,11 8,14.5 M8,1.5 C11,5 11,11 8,14.5" fill="none" stroke="var(--brand-green)" stroke-width="1.2"/></svg>
      www.brimcrestnutrition.example.com.au
    </li>
  </ul>
</section>

<section class="card card--athlete" aria-label="Athlete card">
  <div class="card-texture" role="img" aria-label="Dark honeycomb carbon texture"></div>
  <p class="discount">Discount Code: <span class="discount__code">xxx123</span></p>
  <div class="brand-name">
    <span class="brand-name__main">Brimcrest</span>
    <span class="brand-name__sub">Nutrition</span>
  </div>
  <p class="website">www.brimcrestnutrition.example.com.au</p>
  <p class="social"><span class="social__mark"></span>www.socialsite.example/BrimcrestNutrition</p>
</section>

</body>
</html>
```